Board to put on a meditation centre - Lantern Grove

I need a board design for a new meditation centre based in Oslo which offers free courses in meditation and self-empowerment. The size of the board is width 374cm x height 104cm.  The name of the meditation centre together with subtitles should be on the board but also some elegant decoration that matches the theme (lantern grove/meditation).
Here is the website of the meditation centre to give you a feeling of it: https://lyktelundsenteret.no/
Good if you can use a blue color close to this one: rgb(37, 180, 193) as well as some brown/golden color (similar to the palette on the website).
On the board it should say:
Lyktelunden (in big letters, the rest is subtitles)
Meditasjon & Spirituell visdom
Kurs - Retreat - Dialog
lyktelundsenteret.no
The design should be very elegant and beautiful and the feeling should be of "An Lantern Grove". A logo is here attached and should be used but I need to get a better quality version of it, will upload that as soon as possible.

```html
<!DOCTYPE html>
<html lang="no">
<head>
<meta charset="UTF-8">
<title>Lyktelunden – skilt</title>
<link rel="stylesheet" href="https://fonts.googleapis.com/css2?family=Playfair+Display:ital,wght@1,400&family=Montserrat:wght@500;600&display=swap">
<style>
  :root {
    --page: #ffffff;
    --teal: #07b3c1;
    --teal-deep: #049aa7;
    --ornament-core: rgba(255, 255, 255, 0.62);
    --ornament-mid: rgba(255, 255, 255, 0.38);
    --ornament-edge: rgba(255, 255, 255, 0.18);
    --gold-light: #ffe66b;
    --gold: #f2c31c;
    --gold-deep: #d99a0c;
    --white: #ffffff;
    --ink: #1f1f1f;
    --marker: #e0252b;
  }
  * { margin: 0; padding: 0; box-sizing: border-box; }
  html, body {
    width: 1200px;
    height: 632px;
    overflow: hidden;
    background: var(--page);
  }
  .canvas {
    position: relative;
    width: 1200px;
    height: 632px;
  }
  .board {
    position: absolute;
    left: 53px;
    top: 166px;
    width: 1090px;
    height: 303px;
    background: var(--teal);
    overflow: hidden;
  }
  .ornament {
    position: absolute;
    top: -40px;
    width: 383px;
    height: 383px;
    border-radius: 50%;
    background: radial-gradient(circle at 50% 50%,
      var(--ornament-core) 0%,
      var(--ornament-mid) 45%,
      var(--ornament-edge) 88%,
      rgba(255, 255, 255, 0) 100%);
  }
  .ornament--left { left: -196px; }
  .ornament--right { right: -196px; }
  .board-title {
    position: absolute;
    left: 0;
    right: 0;
    top: 18px;
    text-align: center;
    font-family: "Playfair Display", Georgia, serif;
    font-style: italic;
    font-weight: 400;
    font-size: 108px;
    line-height: 1.2;
    background: linear-gradient(180deg, var(--gold-light) 0%, var(--gold) 55%, var(--gold-deep) 100%);
    -webkit-background-clip: text;
    background-clip: text;
    color: transparent;
    filter: drop-shadow(2px 3px 0 var(--teal-deep));
  }
  .board-subtitles {
    position: absolute;
    left: 0;
    right: 0;
    top: 156px;
    text-align: center;
    font-family: "Montserrat", Arial, sans-serif;
    font-weight: 600;
    font-size: 26px;
    line-height: 29px;
    color: var(--white);
  }
  .board-web {
    position: absolute;
    left: 0;
    right: 0;
    top: 255px;
    display: flex;
    justify-content: center;
    align-items: center;
    gap: 7px;
    font-family: "Montserrat", Arial, sans-serif;
    font-weight: 500;
    font-size: 14px;
    color: var(--ink);
  }
  .board-web__dot {
    width: 22px;
    height: 22px;
    border-radius: 50%;
    background: var(--marker);
  }
</style>
</head>
<body>
  <main class="canvas">
    <section class="board">
      <div class="ornament ornament--left" role="img" aria-label="Hvitt mandala-ornament i halv sirkel langs venstre kant"></div>
      <div class="ornament ornament--right" role="img" aria-label="Hvitt mandala-ornament i halv sirkel langs høyre kant"></div>

      <h1 class="board-title">Lyktelunden</h1>

      <p class="board-subtitles">
        Meditasjon &amp; Spirituell visdom<br>
        Kurs - Retreat - Dialog
      </p>

      <p class="board-web">
        <span class="board-web__dot" aria-hidden="true"></span>
        <span>lyktelundsenteret.no</span>
      </p>
    </section>
  </main>
</body>
</html>
```